Our companies name is The Gilded Ladle and we specialize in craft cupcakes, what I mean by that is that we bake our cupcakes with craft beer and other alcoholic drinks. We are trying to focus on being elegant but at the same time unpretentious. Since we are incorporating beer in our cupcakes we want the business card to have our logo in the front and our information in the back.

Once we select the best design we will provide the contact information to be added. Thank you.

Industry/Entity Type

Business

Font styles to use
Decorative
Script

Requirements
Must have
• Round corners
Should not have
• Square corners

```html
<!DOCTYPE html>
<html lang="en">
<head>
<meta charset="utf-8">
<title>The Gilded Ladle — Business Card</title>
<link rel="stylesheet" href="https://fonts.googleapis.com/css2?family=Exo+2:wght@400;500;600&display=swap">
<style>
  :root {
    --page: #ece9e4;
    --card: #ffffff;
    --card-shade: #ececec;
    --ink: #2b2b2b;
    --ink-soft: #555555;
    --black: #111111;
    --orange: #f05a28;
    --orange-soft: #f7a58a;
    --orange-pale: #fbd9cc;
  }
  * { box-sizing: border-box; margin: 0; padding: 0; }
  html, body {
    width: 1200px; height: 828px; overflow: hidden;
    background: var(--page);
    font-family: "Exo 2", sans-serif;
    color: var(--ink);
  }
  .sheet {
    width: 1200px; height: 828px;
    display: flex; align-items: center; justify-content: center; gap: 40px;
  }
  .card {
    position: relative;
    width: 540px; height: 310px;
    border-radius: 18px;
    overflow: hidden;
    background: radial-gradient(ellipse at 55% 60%, var(--card) 40%, var(--card-shade) 100%);
    box-shadow: 0 10px 28px rgba(0,0,0,0.16);
  }
  .card-art { position: absolute; inset: 0; width: 100%; height: 100%; }

  .brand {
    position: absolute;
    display: flex; align-items: center; gap: 10px;
    font-weight: 600; color: var(--ink);
    letter-spacing: 0.02em;
  }
  .brand-dot {
    border-radius: 50%;
    background: var(--orange);
    flex: none;
  }
  .card-front .brand { left: 36px; bottom: 42px; font-size: 24px; }
  .card-front .brand-dot { width: 22px; height: 22px; }
  .card-back .brand { left: 268px; bottom: 26px; font-size: 15px; gap: 7px; }
  .card-back .brand-dot { width: 14px; height: 14px; }

  .contact {
    position: absolute; right: 30px; top: 30px;
    text-align: right;
  }
  .contact-name {
    font-size: 21px; font-weight: 500; letter-spacing: 0.06em;
    color: var(--orange); line-height: 1;
  }
  .contact-role {
    font-size: 13px; font-weight: 500; letter-spacing: 0.1em;
    color: var(--ink); margin-top: 4px;
  }
  .contact-address {
    font-size: 13px; line-height: 1.35; color: var(--ink);
    margin-top: 20px; font-style: normal;
  }
  .contact-lines { list-style: none; margin-top: 14px; }
  .contact-lines li {
    display: flex; justify-content: flex-end; align-items: center; gap: 6px;
    font-size: 10.5px; line-height: 1.75; color: var(--ink-soft);
  }
  .contact-icon { width: 10px; height: 10px; flex: none; }
  .contact-lines .plain { padding-right: 0; }
</style>
</head>
<body>
<main class="sheet">

  <!-- Front -->
  <section class="card card-front" aria-label="Business card front">
    <svg class="card-art" viewBox="0 0 540 310" preserveAspectRatio="none" aria-hidden="true">
      <defs>
        <linearGradient id="front-glow" x1="0" y1="0" x2="1" y2="0">
          <stop offset="0" stop-color="#f05a28" stop-opacity="0.85"/>
          <stop offset="0.6" stop-color="#f7a58a" stop-opacity="0.35"/>
          <stop offset="1" stop-color="#ffffff" stop-opacity="0"/>
        </linearGradient>
      </defs>
      <path d="M258 0 C300 40 360 60 420 70 C470 78 510 90 540 120 L540 90 C500 60 460 45 410 38 C360 30 320 18 300 0 Z" fill="url(#front-glow)"/>
      <path d="M250 0 C290 45 360 72 430 84 C480 92 515 105 540 128" fill="none" stroke="#111111" stroke-width="5"/>
      <path d="M262 0 C300 38 360 60 425 74 C478 84 515 98 540 118" fill="none" stroke="#f05a28" stroke-width="2"/>
    </svg>
    <div class="brand"><span class="brand-dot"></span>The Gilded Ladle</div>
  </section>

  <!-- Back -->
  <section class="card card-back" aria-label="Business card back">
    <svg class="card-art" viewBox="0 0 540 310" preserveAspectRatio="none" aria-hidden="true">
      <defs>
        <linearGradient id="back-black" x1="0" y1="0" x2="1" y2="1">
          <stop offset="0" stop-color="#2a2a2a"/>
          <stop offset="1" stop-color="#050505"/>
        </linearGradient>
        <linearGradient id="back-glow" x1="0" y1="0" x2="1" y2="0">
          <stop offset="0" stop-color="#f7a58a" stop-opacity="0.8"/>
          <stop offset="1" stop-color="#ffffff" stop-opacity="0"/>
        </linearGradient>
      </defs>
      <path d="M215 0 C255 70 280 130 262 200 C250 250 262 285 290 310 L248 310 C215 280 205 240 215 190 C232 120 210 60 165 0 Z" fill="url(#back-glow)"/>
      <path d="M0 0 H160 C205 55 225 120 208 190 C198 240 210 280 236 310 H0 Z" fill="url(#back-black)"/>
      <path d="M160 0 C205 55 225 120 208 190 C198 240 210 280 236 310" fill="none" stroke="#f05a28" stroke-width="7"/>
      <path d="M176 0 C220 58 238 124 222 192 C212 240 224 280 250 310" fill="none" stroke="#f7a58a" stroke-width="3"/>
    </svg>

    <div class="contact">
      <h1 class="contact-name">NORA PELL</h1>
      <p class="contact-role">DIRECTOR</p>
      <address class="contact-address">214 Copper Row<br>Malt Lane BRK</address>
      <ul class="contact-lines">
        <li>014 562 3390
          <svg class="contact-icon" viewBox="0 0 10 10" aria-hidden="true"><path d="M2 1 L4 1 L4.6 3 L3.5 4 C4 5.2 4.8 6 6 6.5 L7 5.4 L9 6 L9 8 C9 8.6 8.6 9 8 9 C4.5 9 1 5.5 1 2 C1 1.4 1.4 1 2 1 Z" fill="#f05a28"/></svg>
        </li>
        <li>014 562 3391
          <svg class="contact-icon" viewBox="0 0 10 10" aria-hidden="true"><rect x="2.5" y="0.5" width="5" height="9" rx="1" fill="none" stroke="#f05a28" stroke-width="1.2"/><circle cx="5" cy="7.8" r="0.6" fill="#f05a28"/></svg>
        </li>
        <li>014 562 3392
          <svg class="contact-icon" viewBox="0 0 10 10" aria-hidden="true"><rect x="1" y="3" width="8" height="5" rx="1" fill="#f05a28"/><rect x="3" y="1" width="4" height="2.5" fill="none" stroke="#f05a28" stroke-width="1"/></svg>
        </li>
        <li>hello@gildedladle.com
          <svg class="contact-icon" viewBox="0 0 10 10" aria-hidden="true"><rect x="0.8" y="2" width="8.4" height="6" rx="0.8" fill="#f05a28"/><path d="M1 2.4 L5 5.4 L9 2.4" fill="none" stroke="#ffffff" stroke-width="0.9"/></svg>
        </li>
        <li>www.gildedladle.com
          <svg class="contact-icon" viewBox="0 0 10 10" aria-hidden="true"><circle cx="5" cy="5" r="4.2" fill="none" stroke="#f05a28" stroke-width="1"/><ellipse cx="5" cy="5" rx="1.8" ry="4.2" fill="none" stroke="#f05a28" stroke-width="0.8"/><path d="M1 5 H9" stroke="#f05a28" stroke-width="0.8"/></svg>
        </li>
      </ul>
    </div>

    <div class="brand"><span class="brand-dot"></span>The Gilded Ladle</div>
  </section>

</main>
</body>
</html>
```